Weaving Tales Past Screens

We are running an international event in Switzerland on "Transmedia" with some of the hottest names in this hot media space ...

There will be 15 Keynote addresses and we are paying to have them professionally transcribed, copywritten, and proof-read to be published in an eBook.

The 15 Keynotes reference a huge number of global media brands - have a look: www.quorvanthub.com

We want a riveting, beautifully designed eBook cover and layout strategy - with the idea that this will be first of a series we will publish on different "Creative Industries" professional development issues - so MOST important is to think of the ARCHITECTURE of the artwork, as well as the graphic design ... think of the idea of an "imprint" in traditional book publishing - the architecture will remain the same, but the artwork and imagry will change each time.

Core values: Global media, Excellence, World's Best practitioners, Know How-to, Instant Inside Knowledge.

Target Market(s)

Professional Development for International Creative Industries Practitioners.

Industry/Entity Type

Graphic Design

Requirements
Must have
• Should be re-purposable across all other forms of media: it's "Transmedia", right? It should incorporate artwork, design, operate as a logo, typeface and font, and a basic imprint for a series of eBooks

The most important consideration in buying an Book is the Table of Content and the authors (we've got that in gold!) - The second-most important consideration is the artwork on the cover ... it has to be instantly convincing.

```html
<!DOCTYPE html>
<html lang="en">
<head>
<meta charset="utf-8">
<title>Weaving Tales Past Screens – Book Cover</title>
<link href="https://fonts.googleapis.com/css2?family=Oswald:wght@500;700&family=Questrial&display=swap" rel="stylesheet">
<style>
  :root {
    --stage: #e4e4e6;
    --cover: #18181b;
    --cover-edge: #101012;
    --red: #e3202a;
    --red-dark: #b3161e;
    --white: #ffffff;
    --muted-box: #2f2f33;
    --muted-text: #b9b9bd;
    --photo-deep: #1c2740;
    --photo-mid: #3a4e72;
    --photo-glow: #c04a9a;
  }
  * { box-sizing: border-box; margin: 0; padding: 0; }
  html, body {
    width: 1200px; height: 800px; overflow: hidden;
    background: radial-gradient(ellipse at 50% 40%, #f1f1f2 0%, var(--stage) 70%);
    font-family: "Questrial", "Century Gothic", sans-serif;
  }
  .stage { position: relative; width: 1200px; height: 800px; }

  /* Back cover */
  .back-cover {
    position: absolute; left: 140px; top: 90px; width: 400px; height: 620px;
    background: var(--cover);
    border-top: 5px solid var(--red);
    border-bottom: 4px solid var(--red);
    padding: 14px 34px 0;
    color: var(--white);
  }
  .back-cover .author {
    text-align: center; font-size: 11px; margin-left: 120px;
  }
  .back-cover .title {
    font-family: "Oswald", "Arial Narrow", sans-serif; font-weight: 700;
    color: var(--red); text-transform: uppercase; text-align: center;
    font-size: 40px; line-height: 1.0; margin-top: 4px;
    text-shadow: 0 1px 0 var(--red-dark);
  }
  .back-cover .blurb {
    margin-top: 14px; font-size: 10.8px; line-height: 1.5;
    text-align: justify; text-align-last: center;
  }
  .back-cover .marks {
    position: absolute; left: 40px; right: 40px; bottom: 22px;
    display: flex; justify-content: space-between;
  }
  .back-cover .mark-box {
    width: 96px; height: 46px; background: var(--muted-box);
    color: var(--muted-text); font-size: 11px;
    display: flex; align-items: center; justify-content: center;
  }

  /* Spine */
  .spine {
    position: absolute; left: 610px; top: 90px; width: 30px; height: 620px;
    background: var(--cover-edge);
    border-top: 5px solid var(--red);
    display: flex; flex-direction: column; align-items: center;
    justify-content: space-between; padding: 14px 0 10px;
  }
  .spine .spine-title {
    writing-mode: vertical-rl;
    font-family: "Oswald", "Arial Narrow", sans-serif; font-weight: 700;
    color: var(--red); font-size: 21px; letter-spacing: 0.5px;
    text-transform: uppercase; white-space: nowrap;
  }
  .spine .spine-author {
    writing-mode: vertical-rl; color: var(--white); font-size: 9px; white-space: nowrap;
  }

  /* Front cover */
  .front-cover {
    position: absolute; left: 640px; top: 90px; width: 420px; height: 620px;
    background: var(--cover);
    border-top: 5px solid var(--red);
    overflow: hidden;
  }
  .front-cover .headline {
    position: absolute; left: 22px; top: 28px;
    font-family: "Oswald", "Arial Narrow", sans-serif; font-weight: 700;
    color: var(--red); text-transform: uppercase;
    font-size: 58px; line-height: 1; letter-spacing: 2px;
    text-shadow: 1px 1px 0 var(--white);
  }
  .front-cover .stack {
    position: absolute; right: 16px; top: 18px; width: 46px;
    display: flex; flex-direction: column; align-items: center;
    font-family: "Oswald", "Arial Narrow", sans-serif; font-weight: 700;
    color: var(--red); text-transform: uppercase;
    text-shadow: 1px 1px 0 var(--white);
  }
  .front-cover .stack .small-word,
  .front-cover .stack .tall-word {
    display: flex; flex-direction: column; align-items: center;
  }
  .front-cover .stack .small-word { font-size: 20px; line-height: 22px; margin-bottom: 8px; }
  .front-cover .stack .tall-word { font-size: 46px; line-height: 56px; }
  .front-cover .cover-photo {
    position: absolute; left: 22px; top: 160px; width: 330px; height: 414px;
  }
  .front-cover .author-band {
    position: absolute; left: 0; right: 0; bottom: 0; height: 46px;
    background: var(--red); color: var(--white);
    display: flex; align-items: center; justify-content: center;
    font-size: 13px;
  }
</style>
</head>
<body>
<main class="stage">

  <section class="back-cover">
    <p class="author">Author's Name</p>
    <h2 class="title">Weaving Tales<br>Past Screens</h2>
    <p class="blurb">Lorem ipsum dolor sit amet, consectetur adipisicing elit, sed do eiusmod tempor incididunt ut labore et dolore magna aliqua. Ut enim ad minim veniam, quis nostrud exercitation. Lorem ipsum dolor sit amet, consectetur adipisicing elit, sed do eiusmod tempor incididunt ut labore et dolore magna aliqua. Ut enim ad minim veniam, quis nostrud exercitation. Lorem ipsum dolor sit amet, consectetur adipisicing elit, sed do eiusmod tempor incididunt ut labore et dolore magna aliqua. Ut enim ad minim veniam, quis nostrud exercitation. Lorem ipsum dolor sit amet, consectetur adipisicing elit, sed do eiusmod tempor incididunt ut labore et dolore magna aliqua. Ut enim ad minim veniam, quis nostrud exercitation. Lorem ipsum dolor sit amet, consectetur adipisicing elit, sed do eiusmod tempor incididunt ut labore et dolore magna aliqua. Ut enim ad minim veniam, quis nostrud exercitation. Lorem ipsum dolor sit amet, consectetur adipisicing elit, sed do eiusmod tempor incididunt ut labore et dolore magna aliqua. Ut enim ad minim veniam, quis nostrud exercitation. Lorem ipsum dolor sit amet, consectetur adipisicing elit, sed do eiusmod tempor incididunt ut labore et dolore magna aliqua. Ut enim ad minim veniam, quis nostrud exercitation.</p>
    <div class="marks">
      <div class="mark-box">LOGO</div>
      <div class="mark-box">ISBN</div>
    </div>
  </section>

  <aside class="spine">
    <span class="spine-title">Weaving Tales Past Screens</span>
    <span class="spine-author">Author's Name</span>
  </aside>

  <section class="front-cover">
    <h1 class="headline">Weaving<br>Tales</h1>
    <div class="stack">
      <span class="small-word"><span>P</span><span>A</span><span>S</span><span>T</span></span>
      <span class="tall-word"><span>S</span><span>C</span><span>R</span><span>E</span><span>E</span><span>N</span><span>S</span></span>
    </div>
    <svg class="cover-photo" viewBox="0 0 330 414" role="img" aria-label="Cover photograph: an astonished young man in a hooded top holding a tablet that bursts with pink and blue light">
      <defs>
        <radialGradient id="photoGlow" cx="50%" cy="45%" r="65%">
          <stop offset="0%" stop-color="var(--photo-mid)"/>
          <stop offset="55%" stop-color="var(--photo-deep)"/>
          <stop offset="100%" stop-color="var(--cover)"/>
        </radialGradient>
        <radialGradient id="burst" cx="40%" cy="68%" r="35%">
          <stop offset="0%" stop-color="var(--photo-glow)" stop-opacity="0.55"/>
          <stop offset="100%" stop-color="var(--photo-glow)" stop-opacity="0"/>
        </radialGradient>
      </defs>
      <rect width="330" height="414" fill="url(#photoGlow)"/>
      <rect width="330" height="414" fill="url(#burst)"/>
    </svg>
    <div class="author-band">Author's Name</div>
  </section>

</main>
</body>
</html>
```